Funny Swear Word Adult Coloring Book Cover

Trigger warning: Cover has a not-safe-for-work swear word.
Need a full-color (as opposed to half colored like some coloring book covers) wrap-around cover for an 8 x 10 inch paperback coloring book to be published on Bookvale Press.
Design needs to be very vibrant through use of bright colors and gradients. These examples show the kind of vibrancy I need. I'd like for the background color to be dark (preferably deep blue with some light in it) so that the other colors really stand out and because that kind of design sells very well. I'm looking for jewel colors, like pink, teal, yellow, purple, green, aqua - whatever you think looks good together as long as it really pops. The text could be in a gradient too, like example 3
The concept of cover 1 is my favorite, but I don't like the texture. I also want more glow like in 2 and I like the text gradient and style in 3. The fat script in 1 is good too, but don't like texture. The background or border design should be abstract doodle style or mandala or floral. Not too complex and detailed that it would look like it would be hard to color, however.
1 - https://www.shopbookvale.com/gp/product/Q47LM2WRZT/asin=Q47LM2WRZT&revisionId=&format=4&depth=1
2- https://www.shopbookvale.com/50-Gentle-Petals-Calming-Unwinding/dp/K83TQ5NXDA/
3 - https://www.shopbookvale.com/Simple-Doodles-Grownups-Uplifting-Sayings/dp/R61HW7CJPM/
Title: Stay Bloody Radiant
The words "Bloody Radiant" should be much more prominent than anything else, and I'm looking for a bold script font like in example 1 and 3. I do not want the text to be simply aligned horizontally. I'm looking for angles or curves to make it look more dynamic and interesting.

Target Market(s)

Women ages 30-55

Industry/Entity Type

consumer coloring, craft art activity

Other font styles liked:
• Chunky script on cover

Colors
0054AA
0677BA
7BADD7
CADEEF
E8F1F8
00AB8E
00BBA5
67D7C9
C6EFE9
E9F9F6
FFF300
FFF600
FEFA6F
FFFEC7
FFFEE8
E54698
E96AAD
F1A4CE
F9D9EA
FCEFF6
6B429C
8869AF
B7A5CE
E3DAEB
F3F0F8

Requirements
Must have
• vibrant colors, gradients, jewel colors, readable text that can be read on a thumbnail visible on Bookvale

```html
<!DOCTYPE html>
<html lang="en">
<head>
<meta charset="utf-8">
<title>Stay Bloody Radiant – Coloring Book</title>
<link rel="stylesheet" href="https://fonts.googleapis.com/css2?family=Bowlby+One&family=Cinzel:wght@500&family=Dancing+Script:wght@700&display=swap">
<style>
  :root {
    --orange: #ff5e0e;
    --yellow: #ffc21a;
    --pink: #f0247a;
    --purple: #7b35e0;
    --blue: #3a8df0;
    --navy: #1c1446;
    --white: #ffffff;
    --title-pink: #f2549c;
    --title-depth: #e0357f;
  }
  html, body {
    margin: 0;
    padding: 0;
    overflow: hidden;
    background: var(--navy);
  }
  .cover {
    position: relative;
    width: 963px;
    height: 1200px;
    overflow: hidden;
  }
  .mandala-field {
    position: absolute;
    inset: 0;
    background:
      repeating-conic-gradient(from 0deg at 482px 600px,
        var(--orange) 0deg 9deg, var(--pink) 9deg 13deg,
        var(--purple) 13deg 20deg, var(--yellow) 20deg 30deg),
      var(--purple);
  }
  .mandala-field::before {
    content: "";
    position: absolute;
    inset: 0;
    background:
      radial-gradient(circle at 482px 600px, transparent 0 380px, rgba(123, 53, 224, 0.55) 400px, transparent 470px),
      radial-gradient(circle at 60px 140px, rgba(58, 141, 240, 0.85) 0, transparent 230px),
      radial-gradient(circle at 900px 1080px, rgba(58, 141, 240, 0.85) 0, transparent 230px),
      radial-gradient(circle at 920px 120px, rgba(123, 53, 224, 0.7) 0, transparent 220px),
      radial-gradient(circle at 80px 1100px, rgba(123, 53, 224, 0.7) 0, transparent 220px);
  }
  .title-disc {
    position: absolute;
    left: 121px;
    top: 241px;
    width: 722px;
    height: 722px;
    border-radius: 50%;
    background: var(--navy);
    box-shadow: 0 10px 40px rgba(20, 10, 50, 0.55);
  }
  .title-art {
    position: absolute;
    inset: 0;
    width: 963px;
    height: 1200px;
  }
  .kicker {
    font-family: "Bowlby One", sans-serif;
    font-size: 60px;
    fill: var(--white);
    letter-spacing: 3px;
  }
  .script {
    font-family: "Dancing Script", cursive;
    font-weight: 700;
  }
  .script-depth {
    fill: var(--title-depth);
    stroke: var(--title-depth);
    stroke-width: 8px;
    stroke-linejoin: round;
  }
  .script-face {
    fill: var(--white);
    stroke: var(--title-pink);
    stroke-width: 5px;
    stroke-linejoin: round;
    paint-order: stroke fill;
  }
  .format-label {
    font-family: "Cinzel", serif;
    font-weight: 500;
    font-size: 27px;
    letter-spacing: 3px;
    fill: var(--white);
  }
</style>
</head>
<body>
  <main class="cover">
    <div class="mandala-field" role="img" aria-label="Bright mandala and floral doodle pattern in orange, yellow, pink, purple and blue"></div>
    <div class="title-disc"></div>

    <svg class="title-art" viewBox="0 0 963 1200">
      <defs>
        <path id="kicker-arc" d="M 250 410 Q 380 320 525 345"></path>
        <filter id="neon-glow" x="-20%" y="-40%" width="140%" height="180%">
          <feGaussianBlur in="SourceAlpha" stdDeviation="9" result="blur"></feGaussianBlur>
          <feFlood flood-color="#ff8cc6" flood-opacity="0.85"></feFlood>
          <feComposite in2="blur" operator="in" result="glow"></feComposite>
          <feMerge>
            <feMergeNode in="glow"></feMergeNode>
            <feMergeNode in="SourceGraphic"></feMergeNode>
          </feMerge>
        </filter>
      </defs>

      <text class="kicker"><textPath href="#kicker-arc" startOffset="50%" text-anchor="middle">STAY</textPath></text>

      <g class="script" filter="url(#neon-glow)">
        <g transform="translate(540 500) rotate(-15)">
          <text class="script-depth" x="5" y="7" text-anchor="middle" font-size="170" textLength="470" lengthAdjust="spacingAndGlyphs">Bloody</text>
          <text class="script-face" x="0" y="0" text-anchor="middle" font-size="170" textLength="470" lengthAdjust="spacingAndGlyphs">Bloody</text>
        </g>
        <g transform="translate(485 720) rotate(-20)">
          <text class="script-depth" x="6" y="8" text-anchor="middle" font-size="220" textLength="610" lengthAdjust="spacingAndGlyphs">Radiant</text>
          <text class="script-face" x="0" y="0" text-anchor="middle" font-size="220" textLength="610" lengthAdjust="spacingAndGlyphs">Radiant</text>
        </g>
      </g>

      <text class="format-label" x="482" y="876" text-anchor="middle">COLORING BOOK</text>
    </svg>
  </main>
</body>
</html>
```